Book Cover for Senior Care Agencies

Design a cover [kindle and print] for a book of interviews with home health care agencies, that also has client stories [like a Lantern Tales of Kindness type book]

The title is
Hands That Stay

subtitle
Selecting A Trusted Elder Support Service

The book will have 7 co-authors, so they will need to be listed on the cover
Print book Size 6 x 9

For image, I like the idea of an adult helping their senior parent out... What i am going for is very, clean and crisp yet warm. No cartoons.

I don't tend to like script fonts.
thank you

Target Market(s)

Family members who have senior relatives or parents

Industry/Entity Type

Health Care

Font styles to use
Serif
Sans Serif

Requirements
Should not have
• cartoons

```html
<!DOCTYPE html>
<html lang="en">
<head>
<meta charset="utf-8">
<title>Hands That Stay – Book Cover</title>
<link href="https://fonts.googleapis.com/css2?family=Cinzel:wght@600;700&family=Source+Sans+3:wght@400;600;700&display=swap" rel="stylesheet">
<style>
  :root{
    --back-light:#f6f6f6;
    --back-edge:#e2e2e2;
    --ink:#1e1e1e;
    --heading-green:#2f3f12;
    --spine-green:#6a8a3a;
    --frame-green:#5e7a2e;
    --band:rgba(235,240,225,0.82);
    --white:#ffffff;
    --foliage-dark:#4f6b2c;
    --foliage-mid:#7f9f52;
    --foliage-light:#b4c98f;
    --lawn:#8fb35a;
    --path:#b8b29a;
    --shirt:#7f9fc8;
    --trousers:#d9d4c2;
    --ground:#4a3f2c;
  }
  *{margin:0;padding:0;box-sizing:border-box}
  html,body{width:1200px;height:864px;overflow:hidden;background:#ffffff}
  .cover{position:relative;width:1200px;height:864px;display:flex;font-family:"Source Sans 3",sans-serif;color:var(--ink)}

  /* Back cover */
  .back{position:relative;width:576px;height:864px;background:radial-gradient(ellipse at 50% 45%,var(--back-light) 0%,var(--back-light) 45%,var(--back-edge) 100%)}
  .blurb-heading{position:absolute;top:38px;left:0;width:538px;text-align:center;font-weight:700;font-size:21px;color:var(--heading-green);letter-spacing:.3px}
  .blurb{position:absolute;top:68px;left:35px;width:510px;font-size:15.2px;line-height:19.4px;text-align:justify;hyphens:auto}
  .author-box{position:absolute;top:327px;left:36px;width:514px;height:208px;border:2px solid var(--frame-green);background:linear-gradient(90deg,#efefef,#d9d9d9)}
  .author-photo{position:absolute;left:0;top:0;width:232px;height:204px;background:linear-gradient(160deg,#ececec 0%,#d6d6d6 45%,#3a3a40 80%,#2a2a2e 100%)}
  .author-bio{position:absolute;left:254px;top:16px;width:252px;font-size:13.4px;line-height:17.5px;text-align:justify;hyphens:auto}
  .testimonial{position:absolute;top:605px;left:0;width:538px;text-align:center;font-weight:700;font-size:21px;color:var(--heading-green)}

  /* Spine */
  .spine{position:relative;width:48px;height:864px;background:var(--spine-green)}
  .spine-text{position:absolute;top:37px;left:50%;transform-origin:0 0;transform:translateX(12px) rotate(90deg);white-space:nowrap;color:var(--white);display:flex;align-items:baseline;gap:80px}
  .spine-title{font-family:"Cinzel",serif;font-weight:600;font-size:23.5px;letter-spacing:.5px}
  .spine-subtitle{font-family:"Source Sans 3",sans-serif;font-size:22.5px;letter-spacing:.3px}

  /* Front cover */
  .front{position:relative;width:576px;height:864px;overflow:hidden}
  .front-photo{position:absolute;inset:0;background:
      linear-gradient(180deg,rgba(0,0,0,0) 72%,rgba(18,16,10,.85) 100%),
      radial-gradient(ellipse 28% 36% at 52% 62%,var(--trousers) 0%,rgba(217,212,194,.6) 40%,rgba(217,212,194,0) 100%),
      radial-gradient(ellipse 30% 14% at 52% 44%,var(--shirt) 0%,rgba(127,159,200,.5) 45%,rgba(127,159,200,0) 100%),
      radial-gradient(ellipse 22% 40% at 28% 78%,var(--path) 0%,rgba(184,178,154,0) 100%),
      radial-gradient(ellipse 30% 30% at 15% 52%,var(--lawn) 0%,rgba(143,179,90,0) 100%),
      radial-gradient(ellipse 40% 30% at 50% 12%,var(--foliage-light) 0%,rgba(180,201,143,0) 100%),
      linear-gradient(90deg,var(--foliage-dark) 0%,var(--foliage-mid) 30%,var(--foliage-mid) 70%,var(--foliage-dark) 100%),
      linear-gradient(180deg,#6f9048 0%,#7d9a5c 45%,#5c5a3e 78%,var(--ground) 100%)}
  .title{position:absolute;top:20px;left:0;width:576px;text-align:center;font-family:"Cinzel",serif;font-weight:700;color:var(--white);font-size:92px;line-height:88px;letter-spacing:0}
  .subtitle-band{position:absolute;top:213px;left:0;width:576px;height:43px;background:var(--band);display:flex;align-items:center;justify-content:center}
  .subtitle{font-weight:600;font-size:21.5px;color:var(--heading-green);letter-spacing:.2px;white-space:nowrap}
  .subtitle strong{font-weight:700}
  .authors{position:absolute;left:39px;top:769px;display:grid;grid-template-columns:181px 174px 160px;row-gap:4px;color:var(--white);font-size:20.5px;font-weight:600;letter-spacing:.2px;line-height:23px}
</style>
</head>
<body>
<div class="cover">
  <section class="back">
    <h2 class="blurb-heading">GOOD BOOK BLURB</h2>
    <p class="blurb">Lorem ipsum dolor sit amet, consectetur adipiscing elit. Ut euismod magna enim, sagittis tristique orci condimentum a. Pellentesque a leo ac purus semper vestibulum. Vestibulum condimentum tempor neque, ut facilisis nisl sollicitudin quis. Nam sagittis dignissim luctus. Aliquam pellentesque, turpis ut ullamcorper finibus, nibh arcu semper purus, sed rutrum orci nisi sit amet mauris. Aliquam sodales nunc ac ligula iaculis ultrices. Morbi lobortis enim in quam sodales vehicula. Ut facilisis est turpis, sit amet sagittis neque accumsan vitae. Integer scelerisque dui quis porttitor aliquam. Integer a arcu a turpis dapibus rutrum. Praesent efficitur in lorem non rhoncus. Vivamus bibendum id massa id eleifend. Vestibulum quis purus quis dolor dignissim vehicula. Pellentesque tristique vehicula orci sit amet convallis. Nam sollicitudin urna eget turpis eleifend, sed pulvinar magna fermentum.</p>
    <div class="author-box">
      <div class="author-photo" role="img" aria-label="Portrait of the author in a dark suit, seated with hands clasped"></div>
      <p class="author-bio">Lorem ipsum dolor sit amet, consectetur adipiscing elit. Ut euismod magna enim, sagittis tristique orci condimentum a. Pellentesque a leo ac purus semper vestibulum. Vestibulum condimentum tempor neque, ut facilisis nisl sollicitudin quis. Nam sagittis dignissim luctus. Aliquam pellentesque, turpis ut ullamcorper finibus, nibh arcu semper purus, sed rutrum orci nisi sit amet mauris.</p>
    </div>
    <p class="testimonial">TESTIMONIAL GOES HERE</p>
  </section>

  <section class="spine">
    <div class="spine-text">
      <span class="spine-title">HANDS THAT STAY</span>
      <span class="spine-subtitle">SELECTING A TRUSTED ELDER SUPPORT SERVICE</span>
    </div>
  </section>

  <section class="front">
    <div class="front-photo" role="img" aria-label="Photograph: an adult son with his arm around his elderly father, who walks with a cane along a leafy garden path under green trees"></div>
    <h1 class="title">HANDS<br>THAT STAY</h1>
    <div class="subtitle-band">
      <p class="subtitle">SELECTING A TRUSTED <strong>ELDER SUPPORT SERVICE</strong></p>
    </div>
    <div class="authors">
      <span>AUTHOR NAME1</span><span>AUTHOR NAME2</span><span>AUTHOR NAME3</span>
      <span>AUTHOR NAME4</span><span>AUTHOR NAME5</span><span>AUTHOR NAME6</span>
      <span></span><span>AUTHOR NAME7</span><span></span>
    </div>
  </section>
</div>
</body>
</html>
```